Electrical Busness

We require an a5 flyer that promotes our Electrical business. Things we would like included are;
1) our business name, Brightpath Electrical and Communication
2) Our Electrical license, EC 62073
3) Our ABN, 37 512 906 284
4) Our website, www.ozwirespark.com.au
5) Our Email, info@ozwirespark.com.au
6) Our contact number, 0412 586 027
8) Our logo, I will attach this (can you please change it so the bbackground is white not black)
9) Our colours are red and white and some black
10) 'over 8 years experience'
11) 'call today for a free quote'
12) 'friendly, honest and reliable workmanship'
13) 'local Electrician in your area'
14)' servicing Cannington, Melville, Manning, Thornlie, Victoria Park, Canning Vale, Forrestfeild and many more'
15) 'Renovations, additions, upgrades, new installations, maintenance'
16) 'available 24/7 for emergency call outs'
17) 'LED downlights, smoke alarms, RCDs, smoke detectors, power & USB points, dimmers, data, phone points, switchboard upgrade, security lighting, safety certificate, compliance and safety checks, exit and emergency lighting and many more'
18) 'WA qualified and fully insured'
19) 'GTRO member' (will attach logo)

```html
<!DOCTYPE html>
<html lang="en">
<head>
<meta charset="utf-8">
<title>Brightpath Electrical and Communication – Flyer</title>
<link rel="stylesheet" href="https://fonts.googleapis.com/css2?family=Source+Sans+3:ital,wght@0,400;0,600;0,700;1,600&family=Oswald:wght@600&display=swap">
<style>
  :root {
    --red: #d5242a;
    --red-dark: #b81c21;
    --panel: #3b3b3d;
    --paper: #f1f1f1;
    --ink: #1e1e1e;
    --muted: #d9d9d9;
    --white: #ffffff;
    --member-blue: #1b3f8c;
  }
  * { margin: 0; padding: 0; box-sizing: border-box; }
  html, body { width: 897px; height: 1200px; overflow: hidden; background: var(--paper); }
  body { font-family: "Source Sans 3", Arial, sans-serif; color: var(--ink); }
  .flyer { position: relative; width: 897px; height: 1200px; overflow: hidden; background: var(--paper); }
  .flyer > * { position: absolute; }
  .shapes { left: 0; top: 0; width: 897px; height: 1200px; }

  .brand-title { left: 41px; top: 14px; color: var(--white); font-weight: 700; font-size: 38px; line-height: 46px; letter-spacing: 0.2px; }
  .brand-ids { left: 42px; top: 112px; color: var(--white); font-size: 19px; line-height: 20px; word-spacing: 2px; }
  .brand-ids span { margin-right: 12px; }
  .brand-mark { left: 700px; top: 124px; width: 184px; text-align: center; color: var(--white); font-weight: 700; font-size: 30px; line-height: 32px; }

  .headline { left: 40px; top: 684px; color: var(--red); font-weight: 700; font-size: 27px; line-height: 32px; letter-spacing: -0.2px; }

  .services-title { left: 40px; top: 766px; color: var(--white); font-weight: 700; font-size: 24px; line-height: 28px; }
  .service-list { list-style: none; font-size: 21px; line-height: 28.2px; }
  .service-list li { position: relative; padding-left: 22px; white-space: nowrap; }
  .service-list li::before { content: ""; position: absolute; left: 0; top: 8px; width: 15px; height: 15px; border-radius: 50%; background: var(--red); }
  .service-list li::after { content: ""; position: absolute; left: 3px; top: 12.5px; width: 5px; height: 5px; border-top: 2px solid var(--white); border-right: 2px solid var(--white); transform: rotate(45deg); }
  .service-list.col-a { left: 40px; top: 815px; }
  .service-list.col-b { left: 281px; top: 815px; }

  .member { left: 60px; top: 1042px; display: flex; align-items: center; gap: 8px; color: var(--member-blue); font-weight: 700; font-size: 24px; line-height: 28px; }
  .member-square { width: 22px; height: 22px; background: var(--member-blue); }
  .insured { left: 244px; top: 1057px; font-size: 18px; line-height: 20px; letter-spacing: 0.2px; }

  .panel-text { left: 600px; width: 297px; text-align: center; }
  .tagline { top: 683px; color: var(--muted); font-style: italic; font-weight: 600; font-size: 22px; line-height: 29px; }
  .experience { top: 745px; color: var(--muted); font-size: 15.5px; line-height: 18px; }
  .local { top: 791px; color: var(--white); font-weight: 700; font-size: 19px; line-height: 24.5px; }
  .areas { top: 842px; color: var(--white); font-size: 14.5px; line-height: 19.5px; padding: 0 14px; }

  .contact-list { left: 620px; top: 953px; list-style: none; color: var(--white); font-size: 17px; }
  .contact-list li { display: flex; align-items: center; gap: 8px; height: 32px; }
  .contact-icon { width: 20px; height: 20px; flex: none; }

  .cta { left: 0; top: 1102px; width: 897px; height: 98px; display: flex; align-items: center; justify-content: center; gap: 18px; color: var(--white); font-family: "Oswald", "Arial Narrow", sans-serif; font-weight: 600; font-size: 39px; letter-spacing: 0.3px; }
  .cta-icon { width: 40px; height: 40px; }
</style>
</head>
<body>
<main class="flyer">
  <svg class="shapes" viewBox="0 0 897 1200" aria-hidden="false">
    <defs>
      <linearGradient id="swoosh-grey" x1="0" y1="0" x2="1" y2="0">
        <stop offset="0" stop-color="#ffffff"/>
        <stop offset="0.45" stop-color="#9a9a9a"/>
        <stop offset="1" stop-color="#2a2a2a"/>
      </linearGradient>
      <linearGradient id="room-tones" x1="0" y1="0" x2="1" y2="1">
        <stop offset="0" stop-color="#efe9e0"/>
        <stop offset="0.5" stop-color="#e0cdb2"/>
        <stop offset="1" stop-color="#b89d7c"/>
      </linearGradient>
      <linearGradient id="worker-tones" x1="0" y1="0" x2="1" y2="1">
        <stop offset="0" stop-color="#8d8a86"/>
        <stop offset="1" stop-color="#c0302f"/>
      </linearGradient>
    </defs>

    <rect class="header-band" x="0" y="0" width="897" height="680" fill="var(--red)"/>
    <path class="swoosh-grey" d="M0,148 C220,150 520,170 700,255 C790,298 855,340 897,372 L897,392 C820,330 610,214 360,206 C220,202 90,206 0,210 Z" fill="url(#swoosh-grey)"/>
    <path class="swoosh-black" d="M470,208 C650,228 800,320 897,396 L897,408 C790,332 640,230 470,208 Z" fill="#111"/>

    <g role="img" aria-label="Photo of a bright modern living room with downlights, a wall-mounted TV, speakers and a cream sofa">
      <path class="room-photo" d="M0,212 C110,206 240,201 360,208 C610,216 820,334 897,404 L897,600 L620,600 C420,600 190,618 0,652 Z" fill="url(#room-tones)"/>
    </g>

    <path class="stripe-red" d="M0,652 C190,618 420,600 620,600 L640,600 L640,612 L620,612 C420,612 190,634 0,672 Z" fill="var(--red)"/>
    <rect class="below-photo" x="0" y="672" width="600" height="430" fill="var(--paper)"/>
    <path class="stripe-fill" d="M0,672 C190,634 420,612 620,612 L620,640 L0,690 Z" fill="var(--paper)"/>

    <path class="contact-panel" d="M600,593 H897 V1052 H618 Q600,1052 600,1034 Z" fill="var(--panel)"/>
    <path class="panel-swoosh-red" d="M810,612 C845,625 875,638 897,648 L897,672 C870,658 840,645 810,634 Z" fill="var(--red)"/>
    <path class="panel-swoosh-black" d="M810,600 C845,612 875,625 897,634 L897,646 C870,635 842,622 810,610 Z" fill="#111"/>

    <g role="img" aria-label="Round photo of an electrician in a red shirt working on a switchboard">
      <circle class="worker-photo" cx="743" cy="569" r="100" fill="url(#worker-tones)" stroke="#d0d0d0" stroke-width="5"/>
    </g>

    <path class="services-bar" d="M0,762 H292 Q306,762 306,776 V785 Q306,799 292,799 H0 Z" fill="var(--red)"/>
    <rect class="cta-band" x="0" y="1102" width="897" height="98" fill="var(--red)"/>
  </svg>

  <h1 class="brand-title">Brightpath<br>Electrical and Communication</h1>
  <p class="brand-ids"><span>EC 62073</span>ABN 37 512 906 284</p>
  <p class="brand-mark">Brightpath</p>

  <p class="headline">RENOVATIONS • ADDITIONS • UPGRADES<br>NEW INSTALLATIONS • MAINTENANCE</p>

  <h2 class="services-title">OUR SERVICES</h2>
  <ul class="service-list col-a">
    <li>LED downlights</li>
    <li>Smoke alarms</li>
    <li>RCDs</li>
    <li>Smoke detectors</li>
    <li>Power &amp; USB points</li>
    <li>Dimmers</li>
    <li>Data</li>
  </ul>
  <ul class="service-list col-b">
    <li>Phone points</li>
    <li>Switchboard upgrade</li>
    <li>Security lighting</li>
    <li>Safety certificate</li>
    <li>Compliance &amp; safety checks</li>
    <li>Exit &amp; emergency lighting</li>
    <li>and many more</li>
  </ul>

  <div class="member"><span class="member-square"></span>GTRO</div>
  <p class="insured">WA QUALIFIED AND FULLY INSURED</p>

  <p class="panel-text tagline">Friendly, Honest &amp;<br>Reliable Workmanship</p>
  <p class="panel-text experience">over 8 years experience</p>
  <h3 class="panel-text local">LOCAL ELECTRICIAN<br>IN YOUR AREA</h3>
  <p class="panel-text areas">Servicing Cannington, Melville, Manning, Thornlie, Victoria Park, Canning Vale, Forrestfeild and many more...</p>

  <ul class="contact-list">
    <li>
      <svg class="contact-icon" viewBox="0 0 20 20"><circle cx="10" cy="10" r="10" fill="var(--red)"/><path d="M6.5,5 L8.5,5 L9.3,7.6 L8,8.6 C8.7,10 10,11.3 11.4,12 L12.4,10.7 L15,11.5 L15,13.5 C15,14.2 14.4,14.8 13.6,14.7 C9.5,14.3 5.7,10.5 5.3,6.4 C5.2,5.6 5.8,5 6.5,5 Z" fill="#fff"/></svg>
      0412 586 027
    </li>
    <li>
      <svg class="contact-icon" viewBox="0 0 20 20"><circle cx="10" cy="10" r="10" fill="var(--red)"/><rect x="5" y="6.5" width="10" height="7" fill="#fff"/><path d="M5,6.5 L10,10.5 L15,6.5" fill="none" stroke="var(--red)" stroke-width="1.2"/></svg>
      info@ozwirespark.com.au
    </li>
    <li>
      <svg class="contact-icon" viewBox="0 0 20 20"><circle cx="10" cy="10" r="10" fill="var(--red)"/><g fill="none" stroke="#fff" stroke-width="1.2"><circle cx="10" cy="10" r="5.5"/><ellipse cx="10" cy="10" rx="2.3" ry="5.5"/><path d="M4.5,10 H15.5 M5.3,7.3 H14.7 M5.3,12.7 H14.7"/></g></svg>
      www.ozwirespark.com.au
    </li>
  </ul>

  <p class="cta">
    <span>CALL TODAY FOR A FREE QUOTE</span>
    <svg class="cta-icon" viewBox="0 0 40 40" aria-hidden="true"><circle cx="20" cy="20" r="17.5" fill="none" stroke="#fff" stroke-width="3"/><path d="M13.5,11 L17,11 L18.3,15.5 L16.1,17.2 C17.3,19.6 19.5,21.8 21.9,23 L23.6,20.8 L28,22.1 L28,25.6 C28,26.8 27,27.8 25.7,27.6 C18.7,26.9 12.2,20.4 11.5,13.4 C11.3,12 12.3,11 13.5,11 Z" fill="#fff"/></svg>
    <span>0412 586 027</span>
  </p>
</main>
</body>
</html>
```